Professional window cleaning services business needs a flyer design

We are looking to attract large businesses such as gyms, car dealerships and fast food restaurants.
-Have over 15 years of experience in this business
-We serve customers in Melbourne and all surrounding suburbs
-Specialising in automated periodical services(daily,weekly,monthly, yearly)
-Our current client base consists of major fast food restaurants, car dealerships and residential properties.

Industry/Entity Type

Window Cleaning

Colors
3176b5
fbed22

Requirements
Must have
• Business Details:
• Name: Brisk Window Cleaning
• Phone no:93402657
• website:www.glintora.com.au
• email: admin@glintora.com.au
• mail: PO BOX 2746, Wrenfield Vale, 3184

```html
<!DOCTYPE html>
<html lang="en">
<head>
<meta charset="utf-8">
<title>Brisk Window Cleaning – Flyer</title>
<link href="https://fonts.googleapis.com/css2?family=Open+Sans:wght@400;600;700;800&family=Arimo:wght@400;700&display=swap" rel="stylesheet">
<style>
  :root{
    --brand-blue:#3176b5;
    --light-blue:#5ea9e0;
    --sky:#67b3e6;
    --navy:#1d3f73;
    --brand-yellow:#fbed22;
    --gold:#fbc34a;
    --orange:#f5a623;
    --grey-band:#b9bcc0;
    --footer-top:#7d7f82;
    --footer-bottom:#4a4b4d;
    --white:#ffffff;
    --stage:#3b3b3d;
  }
  *{margin:0;padding:0;box-sizing:border-box}
  html,body{width:1061px;height:1200px;overflow:hidden}
  body{background:var(--stage);position:relative;font-family:"Open Sans",sans-serif}
  .flyer{position:absolute;left:89px;top:30px;width:883px;height:1140px;background:var(--brand-blue);overflow:hidden}

  /* header */
  .header{position:absolute;left:0;top:0;width:883px;height:139px;background:linear-gradient(180deg,#3a80c0,#2b6aa8)}
  .header-shape{position:absolute;left:0;top:0}
  .brand{position:absolute;left:36px;top:14px}
  .brand-name{display:block;font-weight:800;font-size:56px;line-height:64px;color:var(--navy);letter-spacing:1px}
  .brand-tag{display:block;font-weight:700;font-size:16px;line-height:20px;color:var(--navy)}
  .call{position:absolute;right:56px;top:22px;width:260px;text-align:center;color:var(--white)}
  .stars{display:flex;justify-content:center;gap:34px;height:26px}
  .star{display:block;width:24px;height:24px}
  .call-label{font-weight:700;font-size:22px;line-height:30px;margin-top:6px}
  .call-number{font-weight:600;font-size:32px;line-height:38px;color:var(--gold)}

  .strip{position:absolute;left:0;width:883px;height:8px;background:var(--grey-band)}

  /* hero */
  .hero-photo{position:absolute;left:0;top:147px;width:883px;height:315px;background:linear-gradient(160deg,#e4e7ec 0%,#c3c9d3 50%,#7d8794 100%)}
  .badge{position:absolute;left:642px;top:202px;width:206px;height:206px}
  .badge-shape{position:absolute;left:0;top:0}
  .badge-text{position:absolute;left:0;top:0;width:206px;height:206px;display:flex;align-items:center;justify-content:center;text-align:center;font-weight:700;font-size:21px;line-height:26px;color:#3b3b3b;transform:rotate(-12deg)}

  .sectors{position:absolute;left:0;top:462px;width:883px;height:47px;background:linear-gradient(180deg,#4d8fcc,#3176b5);font-family:"Arimo",sans-serif;font-weight:700;font-size:18px;color:var(--white)}
  .sector{position:absolute;top:0;line-height:47px;white-space:nowrap}
  .divider{position:absolute;top:0;width:1px;height:47px;background:rgba(255,255,255,.35)}

  /* body */
  .intro{position:absolute;left:59px;top:548px;width:362px;color:var(--white);font-size:22px;line-height:31px}
  .van-photo{position:absolute;left:492px;top:548px;width:320px;height:190px;border:9px solid var(--white);transform:rotate(-1.5deg);box-shadow:4px 6px 10px rgba(0,0,0,.45);background:linear-gradient(180deg,#b8c0ca 0%,#eef0f2 45%,#d9dce0 65%,#55585e 100%)}

  .services{position:absolute;left:0;top:773px;width:883px}
  .service{position:absolute;top:0;width:200px;text-align:center}
  .service-photo{width:186px;height:186px;margin:0 auto;border-radius:50%;border:8px solid var(--white)}
  .service-label{font-family:"Arimo",sans-serif;font-size:15px;color:var(--white);margin-top:12px;letter-spacing:.3px}

  /* footer */
  .rule{position:absolute;left:0;top:1015px;width:883px;height:9px;background:var(--orange)}
  .footer{position:absolute;left:0;top:1024px;width:883px;height:116px;background:linear-gradient(180deg,var(--footer-top),var(--footer-bottom))}
  .contacts{position:absolute;left:274px;top:13px;color:var(--white);font-size:17px;line-height:25px}
  .contact{display:flex}
  .contact-key{width:68px}
  .contact-sep{width:14px}
  .contact-value{font-weight:700}
  .contact-value.link{text-decoration:underline}
</style>
</head>
<body>
<main class="flyer">
  <header class="header">
    <svg class="header-shape" width="883" height="139" viewBox="0 0 883 139" aria-hidden="true">
      <path d="M0 0 H435 C360 30 330 80 300 139 H0 Z" fill="#67b3e6"/>
      <path d="M0 0 H351 C300 40 280 90 262 139 H0 Z" fill="#fbed22"/>
    </svg>
    <div class="brand">
      <span class="brand-name">Brisk</span>
      <span class="brand-tag">PROFESSIONAL WINDOWS<br>CLEANING</span>
    </div>
    <div class="call">
      <div class="stars">
        <svg class="star" viewBox="0 0 24 24" aria-hidden="true"><path d="M12 1l3.3 7 7.6.9-5.6 5.2 1.5 7.5L12 17.8 5.2 21.6l1.5-7.5L1.1 8.9l7.6-.9z" fill="#5ea9e0"/></svg>
        <svg class="star" viewBox="0 0 24 24" aria-hidden="true"><path d="M12 1l3.3 7 7.6.9-5.6 5.2 1.5 7.5L12 17.8 5.2 21.6l1.5-7.5L1.1 8.9l7.6-.9z" fill="#5ea9e0"/></svg>
        <svg class="star" viewBox="0 0 24 24" aria-hidden="true"><path d="M12 1l3.3 7 7.6.9-5.6 5.2 1.5 7.5L12 17.8 5.2 21.6l1.5-7.5L1.1 8.9l7.6-.9z" fill="#5ea9e0"/></svg>
      </div>
      <div class="call-label">Call Us Now</div>
      <div class="call-number">(03) 9340 2657</div>
    </div>
  </header>

  <div class="strip" style="top:139px"></div>

  <section class="hero-photo" role="img" aria-label="Rope-access window cleaner abseiling down a glass building facade"></section>

  <div class="badge">
    <svg class="badge-shape" width="206" height="206" viewBox="0 0 206 206" aria-hidden="true">
      <defs>
        <radialGradient id="badgeGlow" cx="0.4" cy="0.35" r="0.7">
          <stop offset="0" stop-color="#ffffff" stop-opacity=".9"/>
          <stop offset="1" stop-color="#f7c46a" stop-opacity=".4"/>
        </radialGradient>
      </defs>
      <polygon fill="#f5a623" points="103,0 112,22 128,4 131,28 151,13 148,38 171,28 162,51 187,46 173,67 198,67 179,84 203,91 180,102 203,115 179,122 198,139 173,139 187,160 162,155 171,178 148,168 151,193 131,178 128,202 112,184 103,206 94,184 78,202 75,178 55,193 58,168 35,178 44,155 19,160 33,139 8,139 27,122 3,115 26,102 3,91 27,84 8,67 33,67 19,46 44,51 35,28 58,38 55,13 75,28 78,4 94,22"/>
      <circle cx="103" cy="103" r="74" fill="#fde7b8"/>
      <circle cx="103" cy="103" r="74" fill="url(#badgeGlow)"/>
    </svg>
    <div class="badge-text">Melbourne<br>and all<br>surrounding<br>suburbs</div>
  </div>

  <nav class="sectors">
    <span class="sector" style="left:29px">GYM</span>
    <span class="divider" style="left:115px"></span>
    <span class="sector" style="left:151px">CAR DEALERSHIP</span>
    <span class="divider" style="left:370px"></span>
    <span class="sector" style="left:405px">FAST FOOD FRANCHISE</span>
    <span class="divider" style="left:657px"></span>
    <span class="sector" style="left:705px">RESIDENTIAL</span>
  </nav>

  <div class="strip" style="top:509px"></div>

  <p class="intro">We do work - you relax and take it easy. You get the best job in town, at rates you can afford. If you are not happy with our service, we will come back and clean till you are 100% satisfied</p>

  <div class="van-photo" role="img" aria-label="Company service car with ladders on the roof and the cleaning team standing beside it"></div>

  <section class="services">
    <div class="service" style="left:29px">
      <div class="service-photo" role="img" aria-label="Gloved hand hammering roof shingles" style="background:linear-gradient(150deg,#9a9ea4,#4e5359)"></div>
      <div class="service-label">ROOF REPAIR</div>
    </div>
    <div class="service" style="left:232px">
      <div class="service-photo" role="img" aria-label="Gloved hand clearing leaves from a gutter" style="background:linear-gradient(150deg,#d1bf8e,#5a4a2c)"></div>
      <div class="service-label">GUTTER CLEANING</div>
    </div>
    <div class="service" style="left:434px">
      <div class="service-photo" role="img" aria-label="Cleaners abseiling down a tall glass tower" style="background:linear-gradient(150deg,#a8d0f0,#1f4f8c)"></div>
      <div class="service-label">HIGH RISE</div>
    </div>
    <div class="service" style="left:645px">
      <div class="service-photo" role="img" aria-label="Cleaner washing the windows of a residential property" style="background:linear-gradient(150deg,#e0e4e8,#6b4b3a)"></div>
      <div class="service-label">REAL ESTATE</div>
    </div>
  </section>

  <div class="rule"></div>
  <footer class="footer">
    <div class="contacts">
      <div class="contact"><span class="contact-key">website</span><span class="contact-sep">:</span><span class="contact-value">www.glintora.com.au</span></div>
      <div class="contact"><span class="contact-key">email</span><span class="contact-sep">:</span><span class="contact-value link">admin@glintora.com.au</span></div>
      <div class="contact"><span class="contact-key">mail</span><span class="contact-sep">:</span><span class="contact-value">PO BOX 2746, Wrenfield Vale, 3184</span></div>
    </div>
  </footer>
</main>
</body>
</html>
```